Resume for higher management position in a mechanical/consultant industries application*

I would like to use this resume for getting a higher position interview possibilities. My skills are multi-cultural negotiation, mechanical industry sales, outsourcing to Asia, ability to manage the agent/reseller system, well team player. multi-language Chinese/English/German specialized. Please make the design, professional, comfortable to read atmosphere.

Target Market(s)

management position, sales related

Font styles to use
Serif
Sans Serif

```html
<!DOCTYPE html>
<html lang="en">
<head>
<meta charset="UTF-8">
<title>Lin-Wei Hsu – Resume</title>
<link href="https://fonts.googleapis.com/css2?family=Montserrat:wght@300;400;500&display=swap" rel="stylesheet">
<style>
  :root {
    --sky: #d4e7ed;
    --peach: #fbdcc4;
    --rust: #a84431;
    --ink: #3b3b3b;
    --line: #f0a98b;
    --photo-ring: #fbdcc4;
  }
  * { box-sizing: border-box; margin: 0; padding: 0; }
  html, body { width: 850px; height: 1200px; overflow: hidden; }
  body {
    background: var(--sky);
    font-family: 'Montserrat', Arial, sans-serif;
    color: var(--ink);
    position: relative;
  }
  .canvas { position: relative; width: 850px; height: 1200px; }

  .contact-left { position: absolute; left: 74px; top: 70px; }
  .contact-left .name { color: var(--rust); font-weight: 500; font-size: 21px; margin-bottom: 8px; }
  .contact-left p { font-weight: 300; font-size: 21px; line-height: 26px; }

  .portrait {
    position: absolute; left: 319px; top: 99px; width: 212px; height: 212px;
    border-radius: 50%; border: 7px solid var(--photo-ring);
    background: radial-gradient(circle at 50% 40%, #c9a58c 0%, #8a6a58 45%, #7d2d2d 100%);
  }

  .personal { position: absolute; right: 82px; top: 70px; text-align: right; }
  .personal h2 { color: var(--rust); font-weight: 500; font-size: 21px; margin-bottom: 4px; margin-right: 18px; }
  .personal ul { list-style: none; }
  .personal li {
    color: var(--rust); font-weight: 300; font-size: 21px; line-height: 32.5px;
    display: flex; justify-content: flex-end; align-items: center; gap: 9px;
  }
  .personal li svg { width: 16px; height: 16px; stroke: var(--line); fill: none; stroke-width: 1.2; }

  .band { position: absolute; left: 0; top: 310px; width: 850px; height: 218px; background: var(--peach); }

  .side-label {
    position: absolute; left: 26px;
    writing-mode: vertical-rl; transform: rotate(180deg);
    color: var(--rust); font-weight: 300; font-size: 31px; line-height: 34px;
    letter-spacing: 1px; white-space: nowrap;
  }
  .label-education { top: 320px; height: 202px; }
  .label-summary { top: 550px; height: 166px; left: 30px; }
  .label-currently { top: 834px; height: 194px; left: 30px; }

  .education { position: absolute; left: 112px; top: 328px; width: 642px; font-size: 14px; line-height: 17.8px; }
  .education .hd { color: var(--rust); font-weight: 400; }
  .education .hd-strong { color: var(--rust); font-weight: 500; }
  .education .uni { color: var(--rust); font-weight: 300; }
  .education .block { margin-bottom: 17px; }
  .education b { font-weight: 500; color: #222; }
  .education p { font-weight: 300; }

  .edu-graphics {
    position: absolute; left: 446px; top: 338px; width: 190px; height: 78px;
    background: linear-gradient(90deg, #f6cdb2, #f9d6bf);
    border-radius: 6px;
  }

  .summary {
    position: absolute; left: 75px; top: 552px; width: 675px;
    font-size: 14px; font-weight: 300; line-height: 17.3px; text-align: justify;
  }
  .summary p + p { margin-top: 17px; }

  .experience {
    position: absolute; left: 75px; top: 834px; width: 675px;
    font-size: 14px; font-weight: 300; line-height: 17.7px; text-align: justify;
  }
  .experience .role { margin-bottom: 17px; }
  .experience .role-title { font-weight: 500; color: #222; }
  .experience .spread { letter-spacing: 1.2px; }
</style>
</head>
<body>
<div class="canvas">

  <div class="contact-left">
    <div class="name">Lin-Wei Hsu</div>
    <p>XXXX,</p>
    <p>XXXX, Germany</p>
    <p>xxxxxx@postmail.com</p>
    <p>com/in/xxxx</p>
  </div>

  <div class="portrait" role="img" aria-label="Portrait photo of the candidate"></div>

  <div class="personal">
    <h2>Personal Information</h2>
    <ul>
      <li>Lin-Wei Hsu <svg viewBox="0 0 16 16"><circle cx="8" cy="4.5" r="3"/><path d="M3 15c0-4 2.5-6 5-6s5 2 5 6"/></svg></li>
      <li>01/01/0000 <svg viewBox="0 0 16 16"><rect x="2" y="8" width="12" height="6"/><path d="M2 11h12M8 3v5M8 1.5v0.5"/></svg></li>
      <li>Taiwanese <svg viewBox="0 0 16 16"><path d="M3 15V2l11 4-11 4"/></svg></li>
      <li>xxxxxxxx, Germany <svg viewBox="0 0 16 16"><path d="M8 15s5-5 5-9a5 5 0 0 0-10 0c0 4 5 9 5 9z"/><circle cx="8" cy="6" r="1.8"/></svg></li>
      <li>+901010101010 <svg viewBox="0 0 16 16"><rect x="4" y="1" width="8" height="14" rx="1"/><path d="M4 12h8"/></svg></li>
      <li>xxxxxx@postmail.com <svg viewBox="0 0 16 16"><rect x="1.5" y="3.5" width="13" height="9"/><path d="M1.5 3.5 8 9l6.5-5.5"/></svg></li>
    </ul>
  </div>

  <div class="band"></div>
  <div class="side-label label-education">EDUCATION<br>&amp; SKILL</div>

  <div class="edu-graphics" role="img" aria-label="Illustration of a presenter with a chart and an award badge"></div>

  <div class="education">
    <div class="block">
      <div class="hd">Education:</div>
      <div class="hd-strong">MBA, Lombardy Polytechnic Italy 2011-2012</div>
    </div>
    <div class="block">
      <div class="hd">Bachelor of Chemical engineering,</div>
      <div class="uni">Hsinchu Valley University 2005-2009</div>
    </div>
    <div class="block">
      <p><b>MBA degree from LIT, Lombardy Polytechnic.</b></p>
      <p><b>Specialties:</b> Great experiences in handling business with Chinese-cultural business firms. Multi-national corporation skills (especially in Chinese-speaking market)</p>
    </div>
    <p><b>Multi-language skill:</b> native Chinese speaker/ advanced English/ advanced German</p>
  </div>

  <div class="side-label label-summary">SUMMARY</div>
  <div class="summary">
    <p>Mandarin Chinese German/ English speaker, real machining experiences, OEM skills, trade skill, global sourcing Currently, I am a “Sales manager Asia” of a top German rotary table company. I am in charge of four countries Japan, China, South Korea and Taiwan with 3 agents, more than 20 salemen team.</p>
    <p>As a director of manufacuturing, I have more than 5 years professional experiences in manufacturing metal components by different CNC-machines. I am capable of coding CNC G,M-code, designing the working path of different parts and managing the whole process. I have well-understanding of mechanical outsourcing ecosystem in Taiwan. With deep knowledge of outsourcing metal components to different suppliers in Taiwan. Familiar with coordinating with different industrial processes in order to build the final products. (Black oxidizing, Different anodizing, Chemical polishing, Manganese phosphate coating, Heat treatment, and Different grinding methods) Especially love to build prototype in order to get a high profitable potential products. (from zero to one)</p>
  </div>

  <div class="side-label label-currently">CURRENTLY</div>
  <div class="experience">
    <div class="role">
      <div class="role-title">Sales Manager Asiaxxxxxxxxx 2018-now</div>
      <p>Currently, leading 3 major dealers in Taiwan, Mainland China, South Korea and Japan with more than 20 salesmen team. Vorland Rotary provides rotary tables, trunnions and 2 axis rotary tilt units shall have the best possible technical characteristics in the smallest possible space, is the principle <span class="spread">model for our dividing heads -engineering -manufacturing -and assembly.</span></p>
    </div>
    <div class="role">
      <p><span class="role-title">Director of Manufacturing, Brightpeak Precision Machinery Company 2012-2017</span> Using CNC turn/mill machine to manufacture any mechanical components as customers want. Also providing great total solutions for our clients. Photos shown in my ProfileNet are my products which are made by CNC turn-milling dual spindles machines(trophy is programmed by CAM).</p>
    </div>
    <div class="role">
      <p><span class="role-title">Marketing Analyst, Nordlicht Import Mannheim Germany, 2012 Apr- 2012 Nov</span> Help Nordlicht Import to build their sales/marketing strategy for the new launched product “Slick-Mend” in central Europe.</p>
    </div>
    <div class="role">
      <p><span class="role-title">External consultant, Alpenstone Group Bergamo Italty, 2011 Oct-2012 Mar</span>To improve the Vantage suite(ERP system) of Alpenstone with re-organized procurement process and new standardized KPIs.</p>
    </div>
  </div>

</div>
</body>
</html>
```